Webdesign für Beratung von Firmen zum Thema Radon
Zielgruppe
Firmenname: Lumivelde - Ich informiere und berate als Radon Fachperson, Privatpersonen sowie Firmen zum Thema Radon, und die Gefahren die damit verbunden sind in bestehenden Gebäuden und Neubauten. Die Leistung erfolgt in Form eines ausgearbeiteten Sanierungskonzeptes bzw. bautechnische Maßnahmen beim Neubau.
Aufgabenstellung
Keep it simple and clean, weniger ist mehr. Die beigefügten Info-Grafiken sollen nur als Information dienen zum Thema Radon, und sollen nicht verwendet werden - ich hoffe hier doch besseres Bildmaterial von euch zu bekommen :-)

```html
<!DOCTYPE html>
<html lang="de">
<head>
<meta charset="utf-8">
<title>Lumivelde – Radon Beratung</title>
<link href="https://fonts.googleapis.com/css2?family=Poppins:wght@300;400;500;600;700;800&display=swap" rel="stylesheet">
<style>
:root{
  --green:#3aa935;
  --green-dark:#25925a;
  --teal:#1f8a70;
  --blue:#1f6db5;
  --blue-dark:#185a98;
  --ink:#3a3f44;
  --muted:#6b7075;
  --gray-bg:#f2f2f2;
  --block-gray:#c4c4c4;
  --card-green:#effbec;
  --card-blue:#e9f4fd;
}
*{margin:0;padding:0;box-sizing:border-box}
html,body{width:1200px;height:5227px;overflow:hidden}
body{position:relative;font-family:'Poppins',sans-serif;color:var(--ink);background:#fff}
.abs{position:absolute}
.section{position:absolute;left:0;width:1200px}
.photo{position:absolute}
.title{position:absolute;left:0;width:1200px;text-align:center;font-weight:700;font-size:30px;color:var(--green)}
.title span{border-bottom:2px solid var(--green);padding-bottom:2px}
.lead{position:absolute;left:200px;width:800px;text-align:center;font-size:13px;line-height:22px;color:var(--muted)}
p{font-size:13px;line-height:22px;color:var(--muted)}
h3{font-size:16px;font-weight:600;color:var(--ink)}

/* header */
.header{top:0;height:68px;background:#fff;border-top:3px solid var(--green);box-shadow:0 2px 6px rgba(0,0,0,.06);z-index:5}
.nav a{position:absolute;top:24px;font-size:13px;color:var(--ink);text-decoration:none}
.call-btn{position:absolute;left:922px;top:12px;width:158px;height:40px;border-radius:4px;background:linear-gradient(90deg,var(--green-dark),var(--teal));color:#fff;text-align:center;font-size:14px;font-weight:600;line-height:16px;padding-top:5px}
.call-btn small{display:block;font-size:10px;font-weight:400}
.brand{position:absolute;left:522px;top:0;z-index:6}
.brand-name{position:absolute;left:0;top:66px;width:156px;text-align:center;font-size:15px;font-weight:700;color:var(--green-dark);letter-spacing:1px}
.brand-dot{position:absolute;left:62px;top:22px;width:32px;height:32px;border-radius:50%;background:var(--green)}

/* hero */
.hero{top:68px;height:492px;background:linear-gradient(100deg,#4fb648 0%,#3f9e8a 45%,#3a82c8 100%)}
.hero h1{position:absolute;left:170px;top:152px;font-size:36px;font-weight:700;color:#fff;letter-spacing:1px}
.hero p{position:absolute;left:170px;top:222px;width:480px;color:#fff;font-size:13px}
.outline-btn{position:absolute;border:1.5px solid #fff;border-radius:4px;color:#fff;font-size:15px;text-align:center}
.hero-visual{position:absolute;left:730px;top:88px;width:320px;height:320px;border-radius:20px;background:linear-gradient(150deg,rgba(29,60,85,.55),rgba(29,60,85,.25))}

/* team cards */
.card{position:absolute;top:737px;height:556px}
.card.green{background:var(--card-green);border-bottom:4px solid var(--green-dark)}
.card.blue{background:var(--card-blue);border-bottom:4px solid var(--blue)}
.card .frame{position:absolute;border:2px solid currentColor}
.card h2{position:absolute;left:48px;top:346px;font-size:22px;font-weight:600}
.card p{position:absolute;left:48px;top:390px;width:310px;font-size:12px;line-height:21px}
.card .btn{position:absolute;left:48px;top:492px;width:147px;height:38px;border-radius:4px;color:#fff;font-size:12px;text-align:center;line-height:38px}
.arrow{position:absolute;top:975px}
.dot{position:absolute;top:1343px;height:7px;width:40px;border-radius:4px;background:#d3d3d3}

/* radon items */
.rframe{position:absolute;border:4px solid var(--teal)}
.ritem h3{position:absolute}
.ritem p{position:absolute;width:445px}

/* cta */
.cta{top:2613px;height:205px;background:linear-gradient(90deg,#2f9c3e,var(--teal))}
.cta h2{position:absolute;left:0;width:1200px;top:36px;text-align:center;font-size:22px;font-weight:600;color:#fff;line-height:36px}

/* services */
.services{top:2818px;height:999px;background:var(--gray-bg)}
.gblock{position:absolute;background:var(--block-gray)}
.sphoto{position:absolute;border:8px solid #fff;box-shadow:0 2px 8px rgba(0,0,0,.12)}
.bignum{position:absolute;font-size:190px;font-weight:800;color:#fff;line-height:1}
.svc h3{position:absolute;font-size:22px}
.svc p{position:absolute;width:390px}
.svc h4{position:absolute;font-size:12px;font-weight:600;color:var(--ink)}
.svc ul{position:absolute;list-style:none}
.svc li{font-size:12px;line-height:22px;color:var(--muted);padding-left:14px;position:relative}
.svc li:before{content:"";position:absolute;left:0;top:8px;width:6px;height:6px;background:var(--blue)}

/* references */
.ref{position:absolute;top:4105px;width:270px}
.ref .pic{height:168px}
.ref h4{margin-top:28px;font-size:13px;font-weight:600;color:var(--ink);line-height:22px}
.ref p{margin-top:10px;font-size:12px;line-height:21px}
.ref.faded{opacity:.25}
.sq-btn{position:absolute;top:4482px;width:38px;height:38px;border:2px solid;border-radius:3px}

/* contact */
.contact{top:4558px;height:497px;background:var(--gray-bg)}
.contact h2{position:absolute;left:191px;top:140px;font-size:30px;font-weight:700;color:var(--blue)}
.contact .intro{position:absolute;left:191px;top:192px;width:360px;font-size:13px}
.info{position:absolute;left:199px;border-left:4px solid var(--blue);padding-left:16px;height:52px}
.info b{display:block;font-size:12px;font-weight:600;color:var(--ink);line-height:22px}
.info span{font-size:13px;color:var(--muted);line-height:28px}
.field{position:absolute;left:617px;width:426px;background:#fff;border-radius:3px;font-size:13px;color:#b5b5b5;font-style:italic;padding:16px 20px}
.submit{position:absolute;left:617px;top:379px;width:426px;height:69px;background:var(--blue);border-radius:4px;color:#fff;text-align:center;line-height:69px;font-size:15px;font-weight:600;letter-spacing:8px}

/* footer */
.footer{top:5055px;height:172px;background:var(--blue)}
.footer a{position:absolute;top:64px;font-size:13px;color:#fff;text-decoration:none}
.copy{position:absolute;left:0;bottom:0;width:1200px;height:37px;background:var(--blue-dark);color:#cfe0f2;font-size:10px;text-align:center;line-height:37px}
</style>
</head>
<body>

<header class="section header">
  <nav class="nav">
    <a style="left:170px">Über uns</a>
    <a style="left:270px">Was ist Radon?</a>
    <a style="left:410px">Leistung</a>
    <a style="left:717px">Referenzen</a>
    <a style="left:830px">Kontakt</a>
  </nav>
  <div class="call-btn">(555) 014-2286<small>Jetzt Anrufen</small></div>
</header>
<div class="brand">
  <svg width="156" height="135" viewBox="0 0 156 135"><path d="M0 0H156V100L78 132L0 100Z" fill="#fff" stroke="#e2e2e2"/></svg>
  <div class="brand-dot"></div>
  <div class="brand-name">LUMIVELDE</div>
</div>

<section class="section hero">
  <h1>IONISING RADIATION</h1>
  <p>Nulla Lorem mollit cupidatat irure. Laborum magna nulla duis ullamco cillum dolor. Voluptate exercitation incididunt aliquip deserunt reprehenderit elit laborum.</p>
  <div class="outline-btn" style="left:170px;top:324px;width:158px;height:38px;line-height:35px">Mehr Infos</div>
  <div class="hero-visual" role="img" aria-label="Grafik einer Periodensystem-Kachel für das Element Radon"></div>
</section>

<div class="title" style="top:597px"><span>Über uns</span></div>
<p class="lead" style="top:660px">Radon ist ein sehr bewegliches, radioaktives Edelgas, das man weder sehen, riechen oder schmecken kann. Es entsteht beim radioaktiven Zerfall von Uran. Uran kom</p>

<div class="card blue" style="left:-339px;width:443px;opacity:.35"></div>
<div class="card green" style="left:142px;width:439px;color:var(--green-dark)">
  <div class="frame" style="left:47px;top:55px;width:357px;height:265px"></div>
  <div class="photo" role="img" aria-label="Porträtfoto eines lächelnden Mitarbeiters" style="left:33px;top:55px;width:357px;height:258px;background:linear-gradient(135deg,#c9c0b4,#7c7367)"></div>
  <h2 style="color:var(--ink)">Lena Vormann</h2>
  <p>Amet minim mollit non deserunt ullamco est sit aliqua dolor do amet sint. Velit officia consequat duis enim velit mollit. Exercitation veniam consequat sunt nostrud amet.</p>
  <div class="btn" style="background:var(--green-dark)">Mehr Lesen</div>
</div>
<div class="card blue" style="left:615px;width:443px;color:var(--blue)">
  <div class="frame" style="left:40px;top:55px;width:357px;height:265px"></div>
  <div class="photo" role="img" aria-label="Porträtfoto eines Mitarbeiters vor einem Bücherregal" style="left:56px;top:55px;width:357px;height:258px;background:linear-gradient(135deg,#8a5a44,#3e4c5a)"></div>
  <h2 style="color:var(--ink)">Jonas Keller</h2>
  <p>Amet minim mollit non deserunt ullamco est sit aliqua dolor do amet sint. Velit officia consequat duis enim velit mollit. Exercitation veniam consequat sunt nostrud amet.</p>
  <div class="btn" style="background:var(--green-dark)">Mehr Lesen</div>
</div>
<div class="card green" style="left:1096px;width:443px;opacity:.35"></div>
<svg class="arrow" style="left:80px" width="24" height="40" viewBox="0 0 24 40"><path d="M20 4L6 20L20 36" fill="none" stroke="#1f8a70" stroke-width="5"/></svg>
<svg class="arrow" style="left:1094px" width="24" height="40" viewBox="0 0 24 40"><path d="M4 4L18 20L4 36" fill="none" stroke="#1f8a70" stroke-width="5"/></svg>
<div class="dot" style="left:528px;background:var(--green-dark)"></div>
<div class="dot" style="left:580px"></div>
<div class="dot" style="left:631px"></div>

<div class="title" style="top:1395px"><span>Radon</span></div>
<p class="lead" style="top:1458px">Radon ist ein sehr bewegliches, radioaktives Edelgas, das man weder sehen, riechen oder schmecken kann. Es entsteht beim radioaktiven Zerfall von Uran. Uran kommt zum Beispiel im Erdboden oder in Baumaterialien vor.</p>

<div class="ritem">
  <div class="rframe" style="left:290px;top:1567px;width:299px;height:264px"></div>
  <div class="photo" role="img" aria-label="Gelbes Warnschild mit Strahlensymbol und Aufschrift Radon Gas" style="left:227px;top:1575px;width:285px;height:252px;background:linear-gradient(160deg,#f5d21a,#e2b400)"></div>
  <h3 style="left:623px;top:1590px">Was ist Radon?</h3>
  <p style="left:623px;top:1618px">Aus natürlichem Uran in Böden und Gesteinen entsteht Radon, das sich in Gebäuden ansammeln kann und dort das Lungenkrebsrisiko der Bewohner erhöht. Radon ist ein sehr bewegliches, radioaktives Edelgas, das überall in der Umwelt vorkommt. Bei seinem Zerfall sendet es Strahlung aus. Radon ist nach dem Rauchen eine der wichtigsten Ursachen für Lungenkrebs. Etwa fünf Prozent der Todesfälle durch Lungenkrebs in der Bevölkerung sind nach aktuellen Erkenntnissen auf Radon und seine Zerfallsprodukte in Gebäuden zurückzuführen.</p>
</div>

<div class="ritem">
  <h3 style="left:142px;width:445px;text-align:right;top:1949px">Wo kommt Radon vor?</h3>
  <p style="left:142px;top:1977px;text-align:right">Radon kommt in unterschiedlichen Konzentrationen überall in unserer Umwelt vor. Aus dem Untergrund von Gebäuden gelangt Radon auch in die Innenräume von Häusern, wo es sich anreichern kann. Insbesondere bei seltenem Lüften kann das zu hohen Radon-Konzentrationen führen, die gesundheitsgefährdend sind. Die Radon-Konzentrationen im Boden, in der Luft und in Innenräumen sind lokal und regional unterschiedlich.</p>
  <div class="rframe" style="left:623px;top:1904px;width:293px;height:258px"></div>
  <div class="photo" role="img" aria-label="Illustration eines Hauses mit grünen Pfeilen, die aufsteigendes Gas zeigen" style="left:627px;top:1945px;width:437px;height:211px;background:linear-gradient(160deg,#eef1ec,#9aa39c)"></div>
</div>

<div class="ritem">
  <div class="rframe" style="left:294px;top:2243px;width:293px;height:258px"></div>
  <div class="photo" role="img" aria-label="Foto eines Einfamilienhauses mit Garten" style="left:203px;top:2298px;width:347px;height:215px;background:linear-gradient(160deg,#7f8f7a,#3f5a3a)"></div>
  <h3 style="left:623px;top:2284px">Wie kann ich mich vor Radon schützen?</h3>
  <p style="left:623px;top:2312px">Ist zu viel Radon im Haus, hilft es als Erstmaßnahme, regelmäßig und intensiv zu lüften. Da hohe Radon-Konzentrationen in der Regel dadurch entstehen, dass aus dem Baugrund radonhaltige Bodenluft eindringt, sollten neue Gebäude durchgehend gegen Bodenfeuchte und damit auch gegen das Eindringen von Radon abgedichtet und undichte Stellen in Bestandsgebäuden identifiziert und beseitigt werden.</p>
</div>

<section class="section cta">
  <h2>Kostenlose Kostenvoranschläge und Beratungsgespräche<br>(555) 014-2286</h2>
  <div class="outline-btn" style="left:507px;top:136px;width:185px;height:38px;line-height:35px">Jetzt Anrufen</div>
</section>

<section class="section services svc">
  <div class="abs" style="left:577px;top:62px;font-size:30px;font-weight:700;color:var(--green)"><span style="border-bottom:2px solid var(--green)">Leistung</span></div>

  <div class="gblock" style="left:223px;top:75px;width:317px;height:437px"></div>
  <div class="sphoto" role="img" aria-label="Foto zweier Fachleute bei der Begutachtung" style="left:168px;top:111px;width:338px;height:461px;background:linear-gradient(160deg,#b9b6ae,#4a4640)"></div>
  <div class="bignum" style="left:360px;top:122px">1.</div>
  <h3 style="left:577px;top:199px">Begutachtung und Beratung</h3>
  <p style="left:577px;top:238px">Amet minim mollit non deserunt ullamco est sit aliqua dolor do amet sint. Velit officia consequat duis enim velit mollit. Exercitation veniam consequat sunt nostrud amet.</p>
  <h4 style="left:577px;top:318px">Fachwissen</h4>
  <ul style="left:577px;top:352px">
    <li>Cras ornare tristique elit.</li>
    <li>Vivamus vestibulum ntulla nec ante.</li>
    <li>Praesent placerat risus quis eros.</li>
    <li>Fusce pellentesque suscipit nibh.</li>
    <li>Integer vitae libero ac risus egestas placerat.</li>
  </ul>

  <h3 style="left:179px;top:672px">Sanierung</h3>
  <p style="left:179px;top:711px">Amet minim mollit non deserunt ullamco est sit aliqua dolor do amet sint. Velit officia consequat duis enim velit mollit. Exercitation veniam consequat sunt nostrud amet.</p>
  <h4 style="left:179px;top:792px">Fachwissen</h4>
  <ul style="left:179px;top:826px">
    <li>Cras ornare tristique elit.</li>
    <li>Vivamus vestibulum ntulla nec ante.</li>
    <li>Praesent placerat risus quis eros.</li>
    <li>Fusce pellentesque suscipit nibh.</li>
    <li>Integer vitae libero ac risus egestas placerat.</li>
  </ul>
  <div class="gblock" style="left:755px;top:568px;width:260px;height:431px"></div>
</section>
<div class="gblock" style="left:755px;top:3817px;width:260px;height:16px"></div>
<div class="sphoto" role="img" aria-label="Foto einer Hausfassade mit Radon-Abluftrohr" style="left:646px;top:3423px;width:334px;height:450px;background:linear-gradient(160deg,#6f7880,#3a4148)"></div>
<div class="bignum" style="left:660px;top:3430px">2.</div>

<div class="title" style="top:3941px"><span>Referenzen</span></div>
<p class="lead" style="top:4004px">Aliqua id fugiat nostrud irure ex duis ea quis id quis ad et. Sunt qui esse pariatur duis deserunt mollit dolore cillum minim tempor enim. Elit aute irure tempor cupidatat incididunt sint deserunt ut voluptate aute id deserunt nisi.</p>

<div class="ref faded" style="left:-148px">
  <div class="pic" role="img" aria-label="Foto eines hellen Innenraums" style="background:#c9d3dc"></div>
  <h4 style="text-align:right">Messung</h4>
  <p style="text-align:right">Amet minim mollit non deserunt ullamco est sit aliqua dolor do.</p>
</div>
<div class="ref" style="left:158px">
  <div class="pic" role="img" aria-label="Illustration schwebender Landschaftsinseln mit Gebäuden" style="background:linear-gradient(160deg,#f4f6f5,#b8c6c2);border:1px solid #e3e3e3"></div>
  <h4>Natural radiation in Germany</h4>
  <p>The total natural radiation exposure in Germany, respectively the annual effective dose for members of the public is on average 2.1 millisieverts.</p>
</div>
<div class="ref" style="left:465px">
  <div class="pic" role="img" aria-label="Foto von Gemüse in einem Korb" style="background:linear-gradient(160deg,#8a8478,#3c3a35)"></div>
  <h4>Radionuclides in food</h4>
  <p>All foods contain natural radionuclides. In addition, the Chernobyl accident and the atmospheric nuclear weapons tests gave rise to artificial radionuclides in food in Europe.</p>
</div>
<div class="ref" style="left:771px">
  <div class="pic" role="img" aria-label="Foto einer Hauswand mit Rohr und Garten" style="background:linear-gradient(160deg,#7d9a7a,#55646d)"></div>
  <h4>Where does radioactivity occur in the environment?</h4>
  <p>Radionuclides are found everywhere in the environment. In principle, every individual on earth is naturally exposed to ionising radiation.</p>
</div>
<div class="ref faded" style="left:1076px">
  <div class="pic" role="img" aria-label="Foto eines hellen Raumes" style="background:#d7dcd9"></div>
  <h4 style="font-size:20px;color:#888">Forschung</h4>
  <p>Amet minim mollit non deserunt ullamco est sit amet sint.</p>
</div>
<svg class="sq-btn" style="left:934px;border-color:#bbb" viewBox="0 0 34 34"><path d="M26 17H8M14 11L8 17L14 23" fill="none" stroke="#bbb" stroke-width="2"/></svg>
<svg class="sq-btn" style="left:987px;border-color:#1f6db5" viewBox="0 0 34 34"><path d="M8 17H26M20 11L26 17L20 23" fill="none" stroke="#1f6db5" stroke-width="2"/></svg>

<section class="section contact">
  <h2>Kontakt</h2>
  <p class="intro">Sie können uns jederzeit kontaktieren. Wir werden so schnell wie möglich auf Sie zurückkommen!</p>
  <div class="info" style="top:236px"><b>Address</b><span>48 Lindenweg, Talbrück 73921</span></div>
  <div class="info" style="top:304px"><b>Phone</b><span>(555) 019-4731</span></div>
  <div class="info" style="top:384px"><b>Email</b><span>kontakt@lumivelde.example</span></div>
  <div class="field" style="top:87px;height:65px">Name</div>
  <div class="field" style="top:167px;height:65px">Email</div>
  <div class="field" style="top:247px;height:118px">Message</div>
  <div class="submit">EINREICHEN</div>
</section>

<footer class="section footer">
  <a style="left:221px">AGB</a>
  <a style="left:276px">Impressum</a>
  <a style="left:373px">Datenschutz</a>
  <a style="left:727px;top:60px;font-size:16px">Los geht's! —</a>
  <div class="abs" style="left:845px;top:55px;width:132px;height:35px;background:#2e8ff0;border-radius:3px;color:#fff;font-size:12px;text-align:center;line-height:35px">Jetzt Anrufen</div>
  <div class="copy">© 2022 All Rights Reserved</div>
</footer>

</body>
</html>
```